Van Wrapping design

We are a solar company see our website www.brightvale.com.au
We need a design for a van wrapping.
The van is white and i have attached our logo of the company
The van is a KTR M40
The design needs to be elegent and professional

Target Market(s)

This will be see on the road everyday

Industry/Entity Type

Solar

```html
<!DOCTYPE html>
<html lang="en">
<head>
<meta charset="utf-8">
<title>Brightvale – Van Wrap Design</title>
<link href="https://fonts.googleapis.com/css2?family=Poppins:wght@600;700&display=swap" rel="stylesheet">
<style>
  :root {
    --canvas-bg: #ececea;
    --wrap-white: #f7f7f7;
    --wrap-black: #111111;
    --brand-gold: #e0a21a;
    --gold-light: #f0c24a;
    --gold-deep: #b97f0c;
    --stripe-grey: #e4e4e4;
    --panel-grey: #3a3d42;
    --ink: #151515;
  }
  html, body {
    margin: 0;
    padding: 0;
    width: 1200px;
    height: 1200px;
    overflow: hidden;
    background: var(--canvas-bg);
  }
  .wrap-sheet {
    position: relative;
    width: 1200px;
    height: 1200px;
  }
  .side-view {
    position: absolute;
    left: 159px;
    width: 885px;
    height: 419px;
  }
  .side-view--a { top: 0; }
  .side-view--b { top: 429px; }
  .rear-view {
    position: absolute;
    top: 856px;
    width: 373px;
    height: 344px;
  }
  .rear-view--a { left: 215px; }
  .rear-view--b { left: 616px; }
  .brand-name {
    font-family: "Poppins", sans-serif;
    font-weight: 700;
    fill: var(--brand-gold);
  }
  .contact-text {
    font-family: "Poppins", sans-serif;
    font-weight: 600;
    fill: var(--ink);
  }
</style>
</head>
<body>
<main class="wrap-sheet">

  <svg class="side-view side-view--a" viewBox="0 0 885 419" xmlns="http://www.w3.org/2000/svg">
    <defs>
      <linearGradient id="goldA" x1="0" y1="1" x2="1" y2="0">
        <stop offset="0" stop-color="var(--gold-deep)"/>
        <stop offset="0.5" stop-color="var(--brand-gold)"/>
        <stop offset="1" stop-color="var(--gold-light)"/>
      </linearGradient>
    </defs>
    <rect class="wrap-base" x="20" y="30" width="845" height="360" rx="40" fill="var(--wrap-white)"/>
    <polygon class="solar-field" role="img" aria-label="Solar panel grid texture in gold tones" points="430,390 865,390 865,190" fill="url(#goldA)"/>
    <g class="brand-band" transform="translate(215 330) rotate(-13)">
      <polygon class="swoosh-band" points="-20,-110 330,-110 345,-140 640,-140 640,15 -20,15" fill="var(--wrap-black)"/>
      <rect class="contact-stripe" x="-20" y="15" width="660" height="28" fill="var(--stripe-grey)"/>
      <text class="brand-name" x="15" y="-20" font-size="104" textLength="600" lengthAdjust="spacingAndGlyphs">Brightvale</text>
      <text class="contact-text" x="35" y="35" font-size="17">1300 555 014  |  www.brightvale.com.au</text>
    </g>
  </svg>

  <svg class="side-view side-view--b" viewBox="0 0 885 419" xmlns="http://www.w3.org/2000/svg">
    <defs>
      <linearGradient id="goldB" x1="0" y1="1" x2="1" y2="0">
        <stop offset="0" stop-color="var(--gold-deep)"/>
        <stop offset="0.5" stop-color="var(--brand-gold)"/>
        <stop offset="1" stop-color="var(--gold-light)"/>
      </linearGradient>
    </defs>
    <rect class="wrap-base" x="20" y="30" width="845" height="360" rx="40" fill="var(--wrap-white)"/>
    <polygon class="solar-field" role="img" aria-label="Solar panel grid texture in gold tones" points="400,390 865,390 865,180" fill="url(#goldB)"/>
    <g class="brand-band" transform="translate(205 325) rotate(-14)">
      <polygon class="swoosh-band" points="-20,-115 330,-115 345,-145 640,-145 640,15 -20,15" fill="var(--wrap-black)"/>
      <rect class="contact-stripe" x="-20" y="15" width="660" height="28" fill="var(--stripe-grey)"/>
      <text class="brand-name" x="15" y="-20" font-size="108" textLength="600" lengthAdjust="spacingAndGlyphs">Brightvale</text>
      <text class="contact-text" x="35" y="35" font-size="17">1300 555 014  |  www.brightvale.com.au</text>
    </g>
  </svg>

  <svg class="rear-view rear-view--a" viewBox="0 0 373 344" xmlns="http://www.w3.org/2000/svg">
    <defs>
      <linearGradient id="goldC" x1="0" y1="0" x2="1" y2="1">
        <stop offset="0" stop-color="var(--gold-light)"/>
        <stop offset="1" stop-color="var(--gold-deep)"/>
      </linearGradient>
    </defs>
    <rect class="rear-glass" x="55" y="25" width="263" height="110" rx="18" fill="var(--wrap-black)"/>
    <rect class="rear-strip" x="40" y="135" width="293" height="20" fill="var(--wrap-white)"/>
    <rect class="solar-field" role="img" aria-label="Solar panel grid texture in gold tones" x="45" y="155" width="283" height="165" rx="22" fill="url(#goldC)"/>
    <polygon class="step-block" points="65,132 135,132 135,150 178,150 178,250 70,250" fill="var(--wrap-black)"/>
    <rect class="solar-module" role="img" aria-label="Solar panel module" x="100" y="155" width="64" height="90" fill="var(--panel-grey)"/>
    <text class="brand-name" x="186" y="96" font-size="40" text-anchor="middle">Brightvale</text>
    <text class="contact-text" x="188" y="230" font-size="14">1300 555 014</text>
    <text class="contact-text" x="188" y="247" font-size="10.5">www.brightvale.com.au</text>
  </svg>

  <svg class="rear-view rear-view--b" viewBox="0 0 373 344" xmlns="http://www.w3.org/2000/svg">
    <defs>
      <linearGradient id="goldD" x1="0" y1="0" x2="1" y2="1">
        <stop offset="0" stop-color="var(--gold-light)"/>
        <stop offset="1" stop-color="var(--gold-deep)"/>
      </linearGradient>
    </defs>
    <rect class="rear-glass" x="55" y="25" width="263" height="110" rx="18" fill="var(--wrap-black)"/>
    <rect class="rear-strip" x="40" y="135" width="293" height="20" fill="var(--wrap-white)"/>
    <rect class="solar-field" role="img" aria-label="Solar panel grid texture in gold tones" x="45" y="155" width="283" height="165" rx="22" fill="url(#goldD)"/>
    <text class="brand-name" x="186" y="96" font-size="40" text-anchor="middle">Brightvale</text>
    <text class="contact-text" x="186" y="232" font-size="22" text-anchor="middle">1300 555 014</text>
    <text class="contact-text" x="186" y="256" font-size="15" text-anchor="middle">www.brightvale.com.au</text>
  </svg>

</main>
</body>
</html>
```